Business Card Design Project

This is a new division in our company. "Kestrel Wellsite & Safety" This is a Oilfield Safety company. I have included our new logo. I also have given our other business card. We love double sided with lots of color. We like to stand out. Please DO NOT duplicate our other card and bring your design into it. See all attached files.
Reason: forgot to change this when I posted it.
Here is the correct information card.
www.kestrelwellsitesafety.example
Dwayne@kestrelwellsitesafety.example
Reason: revision for a few.
Reason: was traveling and need to review designs.
Target Market(s)
Oil and Gas industry. Masculine look.
Industry/Entity Type
Business
Look and feel

```html
<!DOCTYPE html>
<html lang="en">
<head>
<meta charset="utf-8">
<title>Kestrel Wellsite &amp; Safety – Business Cards</title>
<link href="https://fonts.googleapis.com/css2?family=Source+Sans+3:wght@400;600;700&display=swap" rel="stylesheet">
<style>
  :root {
    --stage: #2a2a2a;
    --white: #ffffff;
    --band-green: #3d9a48;
    --forest: #2e6b38;
    --field-light: #3a9143;
    --field-dark: #1f6a31;
    --teal: #45bfc2;
    --gold: #f2b81f;
    --orange: #f26a2e;
    --safety-red: #e23b2b;
  }
  * { box-sizing: border-box; margin: 0; padding: 0; }
  html, body {
    width: 1200px; height: 1200px; overflow: hidden;
    background: var(--stage);
    font-family: "Source Sans 3", Arial, sans-serif;
  }
  .card {
    position: absolute;
    width: 436px; height: 256px;
    border-radius: 22px;
    overflow: hidden;
  }

  /* Back side */
  .card-back { left: 34px; top: 36px; }
  .back-scene {
    position: absolute; inset: 0;
    background: linear-gradient(160deg, var(--field-light) 0%, #2f8a3e 50%, var(--field-dark) 100%);
  }
  .back-brand {
    position: absolute; left: 0; right: 0; top: 98px;
    text-align: center; color: var(--teal); font-weight: 700;
    text-transform: uppercase; line-height: 1;
  }
  .back-brand .word-main { display: block; font-size: 48px; letter-spacing: 2px; }
  .back-brand .word-sub { display: block; font-size: 19px; letter-spacing: 2px; margin-top: 6px; }
  .tagline {
    position: absolute; left: 58px; top: 199px;
    color: var(--white); font-size: 17px; letter-spacing: .3px;
  }
  .tagline .accent { color: var(--orange); }
  .side-label {
    position: absolute; left: 185px; top: 306px;
    color: var(--white); font-size: 56px; font-weight: 400; letter-spacing: 1px;
  }

  /* Front side */
  .card-front { left: 624px; background: var(--forest); }
  .brand-area {
    height: 109px; background: var(--white);
    padding: 26px 0 0 26px;
    color: var(--teal); font-weight: 700; text-transform: uppercase; line-height: 1;
  }
  .brand-area .word-main { display: block; font-size: 38px; letter-spacing: 2px; }
  .brand-area .word-sub { display: block; font-size: 16px; letter-spacing: 2px; margin-top: 4px; }
  .name-band {
    height: 36px; background: var(--band-green);
    color: var(--gold); font-weight: 700; font-size: 17px;
    text-align: center; line-height: 36px; letter-spacing: .5px;
    text-transform: uppercase;
  }
  .main-phone {
    position: absolute; left: 30px; top: 158px; width: 166px; text-align: center;
    color: var(--gold); font-weight: 700; font-size: 21px;
  }
  .main-phone svg { display: block; margin: 0 auto 4px; }
  .details {
    position: absolute; right: 22px; top: 155px;
    list-style: none; text-align: right;
    color: var(--white); font-size: 12.5px; line-height: 16px;
  }
  .details li { display: flex; justify-content: flex-end; align-items: center; gap: 7px; }
  .details li span { display: block; }
  .details .web { color: var(--orange); font-size: 14px; font-weight: 600; }
  .details svg { flex: none; }
  .details .icon-gap { width: 11px; }
</style>
</head>
<body>

<svg width="0" height="0" style="position:absolute" aria-hidden="true">
  <defs>
    <symbol id="icon-phone" viewBox="0 0 20 16">
      <path d="M1 5c0-3 4-4 9-4s9 1 9 4l-1 2-4-1V4H6v2L2 7z" fill="currentColor"/>
      <rect x="4" y="7" width="12" height="8" rx="1.5" fill="currentColor"/>
      <circle cx="10" cy="11" r="2" fill="#2e6b38"/>
    </symbol>
    <symbol id="icon-pin" viewBox="0 0 10 14">
      <path d="M5 0a5 5 0 0 1 5 5c0 4-5 9-5 9S0 9 0 5a5 5 0 0 1 5-5z" fill="currentColor"/>
      <circle cx="5" cy="5" r="2" fill="#2e6b38"/>
    </symbol>
    <symbol id="icon-mobile" viewBox="0 0 8 12">
      <rect x=".6" y=".6" width="6.8" height="10.8" rx="1" fill="none" stroke="currentColor" stroke-width="1.2"/>
    </symbol>
    <symbol id="icon-mail" viewBox="0 0 10 7">
      <rect width="10" height="7" fill="currentColor"/>
      <path d="M0 0l5 4 5-4" fill="none" stroke="#2e6b38" stroke-width="1"/>
    </symbol>
    <symbol id="icon-globe" viewBox="0 0 12 12">
      <g fill="none" stroke="currentColor" stroke-width="1">
        <circle cx="6" cy="6" r="5.3"/><ellipse cx="6" cy="6" rx="2.3" ry="5.3"/>
        <path d="M.7 6h10.6M1.8 3h8.4M1.8 9h8.4"/>
      </g>
    </symbol>
  </defs>
</svg>

<!-- Back side -->
<section class="card card-back">
  <div class="back-scene" role="img" aria-label="Green-tinted photograph of oil derricks at a wellsite"></div>
  <div class="back-brand">
    <span class="word-main">Kestrel</span>
    <span class="word-sub">Wellsite &amp; Safety</span>
  </div>
  <p class="tagline">For all your <span class="accent">Automation &amp; Safety</span> Needs</p>
</section>
<p class="side-label">Back</p>

<!-- Front sides -->
<section class="card card-front" style="top:36px">
  <div class="brand-area"><span class="word-main">Kestrel</span><span class="word-sub">Wellsite &amp; Safety</span></div>
  <div class="name-band">Colt Ramsey</div>
  <div class="main-phone"><svg width="20" height="16" style="color:var(--safety-red)"><use href="#icon-phone"/></svg>1-800-555-0142</div>
  <ul class="details">
    <li><span>4810 N. Ridge Road</span><svg width="11" height="12" style="color:var(--orange)"><use href="#icon-pin"/></svg></li>
    <li><span>Pinecrest, TX 77000</span><span class="icon-gap"></span></li>
    <li><span>210-555-0134</span><svg width="11" height="11" style="color:var(--orange)"><use href="#icon-mobile"/></svg></li>
    <li><span>ColtR@kestrelwellsitesafety.example</span><svg width="11" height="8" style="color:var(--safety-red)"><use href="#icon-mail"/></svg></li>
    <li class="web"><span>www.kestrelwellsitesafety.example</span><svg width="11" height="11" style="color:var(--orange)"><use href="#icon-globe"/></svg></li>
  </ul>
</section>

<section class="card card-front" style="top:329px">
  <div class="brand-area"><span class="word-main">Kestrel</span><span class="word-sub">Wellsite &amp; Safety</span></div>
  <div class="name-band">Lena Marsh</div>
  <div class="main-phone"><svg width="20" height="16" style="color:var(--safety-red)"><use href="#icon-phone"/></svg>1-800-555-0142</div>
  <ul class="details">
    <li><span>4810 N. Ridge Road</span><svg width="11" height="12" style="color:var(--orange)"><use href="#icon-pin"/></svg></li>
    <li><span>Pinecrest, TX 77000</span><span class="icon-gap"></span></li>
    <li><span>713-555-0185</span><svg width="11" height="11" style="color:var(--orange)"><use href="#icon-mobile"/></svg></li>
    <li><span>Lena@kestrelwellsitesafety.example</span><svg width="11" height="8" style="color:var(--safety-red)"><use href="#icon-mail"/></svg></li>
    <li class="web"><span>www.kestrelwellsitesafety.example</span><svg width="11" height="11" style="color:var(--orange)"><use href="#icon-globe"/></svg></li>
  </ul>
</section>

<section class="card card-front" style="top:617px">
  <div class="brand-area"><span class="word-main">Kestrel</span><span class="word-sub">Wellsite &amp; Safety</span></div>
  <div class="name-band">Wade Ramsey</div>
  <div class="main-phone"><svg width="20" height="16" style="color:var(--safety-red)"><use href="#icon-phone"/></svg>1-800-555-0142</div>
  <ul class="details">
    <li><span>4810 N. Ridge Road</span><svg width="11" height="12" style="color:var(--orange)"><use href="#icon-pin"/></svg></li>
    <li><span>Pinecrest, TX 77000</span><span class="icon-gap"></span></li>
    <li><span>210-555-0136</span><svg width="11" height="11" style="color:var(--orange)"><use href="#icon-mobile"/></svg></li>
    <li><span>WadeR@kestrelwellsitesafety.example</span><svg width="11" height="8" style="color:var(--safety-red)"><use href="#icon-mail"/></svg></li>
    <li class="web"><span>www.kestrelwellsitesafety.example</span><svg width="11" height="11" style="color:var(--orange)"><use href="#icon-globe"/></svg></li>
  </ul>
</section>

<section class="card card-front" style="top:907px">
  <div class="brand-area"><span class="word-main">Kestrel</span><span class="word-sub">Wellsite &amp; Safety</span></div>
  <div class="name-band">Dwayne Marsh</div>
  <div class="main-phone"><svg width="20" height="16" style="color:var(--safety-red)"><use href="#icon-phone"/></svg>1-800-555-0142</div>
  <ul class="details">
    <li><span>4810 N. Ridge Road</span><svg width="11" height="12" style="color:var(--orange)"><use href="#icon-pin"/></svg></li>
    <li><span>Pinecrest, TX 77000</span><span class="icon-gap"></span></li>
    <li><span>713-555-0184</span><svg width="11" height="11" style="color:var(--orange)"><use href="#icon-mobile"/></svg></li>
    <li><span>Dwayne@kestrelwellsitesafety.example</span><svg width="11" height="8" style="color:var(--safety-red)"><use href="#icon-mail"/></svg></li>
    <li class="web"><span>www.kestrelwellsitesafety.example</span><svg width="11" height="11" style="color:var(--orange)"><use href="#icon-globe"/></svg></li>
  </ul>
</section>

</body>
</html>
```